Graphic for The Quill newsletter - Graffiti style font

I need a few different images that have different purposes but are all for an email newsletter I produce, The Quill. One is for social media posting and the other is for use in the newsletter itself as the banner (you can see the front page of the newsletter attached to get a feel for how it has existed to date) and on my website to take people to current and back issues of the newsletter. The Quill is a monthly newsletter with updates on the real estate market in Hudson Valley, New York. Social media postings will be to advertise the newsletter and organically grow with new subscribers. The Quill got its name due to the Hudson Valley being steeped in brickyard history as much of construction in yesteryear was of brick with the Hudson Valley being a center point of manufacture.
1). Image of bricks (like a brick wall) with the words "The Quill". My vision is The Quill image would be of more vintage looking brick wall with the words "The Quill" in almost a hand written graffiti type of font potentially on a slant. I need this as a jpg file that is sized to post on Instagram, Facebook and LinkedIn. The purpose of this one is to catch eye and lead people to click to subscribe.
2) I also need a second banner image for the website and email newsletter that has the same feel but includes "Hudson Valley Real Estate News and Views". If "Hudson Valley Real Estate News and Views" can also fit on the one for social media posting, it would be ideal, but I would opt to exclude the extra words rather than clutter on social media if need be. For the newsletter banner version, I have attached a copy of the last Quill newsletter that went out. I'm looking to replace the current words "The Quill" with an actual image for the next newsletter.
I attached my logo so you can get a feel for the colors. It can contrast with the logo to stand out but it needs to be a complimentary contrast with the colors in the logo so it works in close proximity to it in the newsletter (as you'll see in attached). While it would be ideal to have consistency across platforms, the version for social media can utilize a different color theme if desired as that image will stand alone without proximity to my logo.
Target Market(s)
35-65 male and female
Other font styles liked:
- more on the graffiti side
Requirements
Must have
- Quill wall as backdrop and handwritten on the graffiti style font. For newsletter and website banner it can't clash with my logo as they would be in close proximity of each other. It can complimentary contrast though.
Nice to have
- "Hudson Valley Real Estate News and Views" included as a tagline and descriptor . Along the lines of the attached font, but not. More bold. Less whimsical and more on the graffiti side.

```html
<!DOCTYPE html>
<html lang="en">
<head>
<meta charset="utf-8">
<title>The Quill – January 2021</title>
<link rel="stylesheet" href="https://fonts.googleapis.com/css2?family=Poppins:wght@400;600&family=Rubik+Wet+Paint&family=Oswald:wght@500;600&display=swap">
<style>
  :root {
    --page-bg: #ebe6de;
    --frame-gold: #fdd22c;
    --title-gold: #fcd22a;
    --title-edge: #2a160c;
    --logo-brown: #5a3d12;
    --logo-gold: #c49a2c;
    --brick-dark: #5e2619;
    --brick-mid: #8f3f2b;
    --brick-light: #b0603f;
    --ink: #1d1d1d;
    --paper: #ffffff;
    --chart-grey: #5e5e6a;
  }
  * { box-sizing: border-box; margin: 0; padding: 0; }
  html, body { width: 853px; height: 1200px; overflow: hidden; background: var(--page-bg); }

  .newsletter {
    position: absolute;
    left: 156px; top: 31px;
    width: 600px; height: 1264px;
    transform: scale(0.9);
    transform-origin: top left;
    background: var(--paper);
    border: 10px solid var(--frame-gold);
    font-family: "Poppins", sans-serif;
    color: var(--ink);
  }

  .masthead {
    height: 194px;
    display: flex; align-items: center; justify-content: center; gap: 18px;
  }
  .masthead__dot { width: 58px; height: 58px; border-radius: 50%; background: var(--logo-gold); }
  .masthead__name { font-size: 34px; font-weight: 600; color: var(--logo-brown); letter-spacing: 0.5px; }

  .banner {
    position: relative;
    height: 400px;
    text-align: center;
  }
  .banner__wall {
    position: absolute; inset: 0;
    background: linear-gradient(160deg, var(--brick-dark) 0%, var(--brick-mid) 40%, var(--brick-light) 62%, var(--brick-mid) 82%, var(--brick-dark) 100%);
  }
  .banner__title {
    position: absolute; left: 0; right: 0; top: 118px;
    font-family: "Rubik Wet Paint", cursive;
    font-size: 104px; line-height: 1;
    color: var(--title-gold);
    -webkit-text-stroke: 3px var(--title-edge);
    text-shadow: 4px 5px 0 var(--title-edge);
    transform: rotate(-3deg);
  }
  .banner__tagline {
    position: absolute; left: 0; right: 0; top: 252px;
    font-family: "Oswald", sans-serif; font-weight: 500;
    font-size: 27px; color: #fff;
    text-shadow: 2px 2px 3px rgba(0,0,0,.7);
  }
  .banner__date {
    position: absolute; left: 0; right: 0; top: 300px;
    font-family: "Oswald", sans-serif; font-weight: 600;
    font-size: 28px; letter-spacing: 3px; color: #fff;
    text-shadow: 2px 2px 3px rgba(0,0,0,.7);
  }
  .banner__notch {
    position: absolute; bottom: 0; width: 21px; height: 40px;
    background: var(--logo-gold);
  }
  .banner__notch--left { left: 0; clip-path: polygon(100% 0, 100% 100%, 0 100%); }
  .banner__notch--right { right: 0; clip-path: polygon(0 0, 100% 100%, 0 100%); }

  .intro {
    position: absolute; left: 21px; top: 555px;
    width: 540px; height: 208px;
    background: var(--paper);
    box-shadow: 0 4px 12px rgba(0,0,0,.12);
    padding: 30px 26px 0;
    font-size: 14.5px; line-height: 24px; text-align: center;
  }

  .feature { position: absolute; font-size: 14.5px; line-height: 24px; }
  .feature h2 { font-size: 17.5px; font-weight: 600; letter-spacing: 0.4px; }
  .feature--left { left: 30px; top: 810px; width: 294px; }
  .feature--right { left: 349px; top: 800px; width: 206px; }
  .feature--left h2 { margin: 12px 0 20px; }
  .feature--right h2 { margin: 0 0 22px; }

  .feature__art {
    width: 265px; height: 110px;
    background: linear-gradient(180deg, #f4f4f6 0%, #d9d9de 100%);
    position: relative;
  }
  .feature__art svg { position: absolute; inset: 0; }
</style>
</head>
<body>
  <article class="newsletter">
    <header class="masthead">
      <span class="masthead__dot"></span>
      <span class="masthead__name">Riverbend Home Co</span>
    </header>

    <section class="banner">
      <div class="banner__wall" role="img" aria-label="Vintage red brick wall photograph"></div>
      <h1 class="banner__title">THE QUILL</h1>
      <p class="banner__tagline">Hudson Valley Real Estate News and Views</p>
      <p class="banner__date">JANUARY 2021</p>
      <span class="banner__notch banner__notch--left"></span>
      <span class="banner__notch banner__notch--right"></span>
    </section>

    <section class="intro">
      <p>Lorem ipsum dolor sit amet, consectetur adipiscing elit. Duis finibus magna vel pretium commodo. Nullam vel ante ac eros elementum pretium. Nulla vel ipsum ac lacus sollicitudin sagittis. Ut nisl felis, rutrum at pretium id, pulvinar eget lacus. Cras egestas maximus vehicula. In eget leo placerat, fermentum ipsum vitae, pulvinar massa. Sed nec sem sit amet ligula convallis tincidunt.</p>
    </section>

    <section class="feature feature--left">
      <div class="feature__art" role="img" aria-label="Illustration of a house roof with a rising market chart"></div>
      <h2>Lorem Ipsum Dolor Sit Amet</h2>
      <p>Lorem ipsum dolor sit amet, consectetur adipiscing elit. Duis finibus magna vel pretium commodo. Nullam vel ante ac eros elementum pretium. Nulla vel ipsum ac lacus sollicitudin sagittis. Ut nisl felis, rutrum at pretium id, pulvinar eget lacus. Cras egestas maximus vehicula. In eget leo placerat, fermentum ipsum vitae, pulvinar massa. Sed nec sem sit amet ligula convallis tincidunt.</p>
    </section>

    <section class="feature feature--right">
      <h2>Lorem Ipsum Dolor</h2>
      <p>Lorem ipsum dolor sit amet, consectetur adipiscing elit. Duis finibus magna vel pretium commodo. Nullam vel ante ac eros elementum pretium. Nulla vel ipsum ac lacus sollicitudin sagittis. Ut nisl felis, rutrum at pretium id, pulvinar eget lacus. Cras egestas maximus vehicula. In eget leo placerat, fermentum ipsum vitae,</p>
    </section>
  </article>
</body>
</html>
```